Meadowtail Pet Business Card

We need a business card designed with two sides to it. I would like the front of the card to be mostly graphic and the back of the card to have the bullet points of our pet food.

I don't have a telephone number for the business yet so just leave a space for a toll free number. (800) xxx-xxxx.

Thanks,

Tobias

Combination Diet
Chicken Diet
Beef Diet
Lamb Diet

Website:  www.meadowtailpet-example.net

email:  rwelby@meadowtailpet-example.net

Direct - 347-xxx-xxxx
Toll Free - xxx-xxx-xxxx

www.meadowtailpet-example.net

Ravi Welby (Example)
Customer Experience Officer

rwelby@meadowtailpet-example.net
Direct - (347) xxx-xxxx

Sales Inquiries - (800) xxx-xxxx

All,

Please include the following items on the back of the business card.

Combination Diet
Chicken Diet
Beef Diet
Lamb Diet
 

Thanks,

Tobias

All, I will also want a QR code on the front or back of the card that can be scanned by a smart phone with our individual contact information.  Thanks, Tobias

Industry/Entity Type

Pet

```html
<!DOCTYPE html>
<html lang="en">
<head>
<meta charset="utf-8">
<title>Meadowtail Pet Business Card</title>
<link rel="stylesheet" href="https://fonts.googleapis.com/css2?family=PT+Sans:wght@400;700&display=swap">
<style>
  :root {
    --bark: #2a1710;
    --amber: #e98a26;
    --amber-text: #f0922c;
    --white: #ffffff;
    --page: #ffffff;
    --label: #333333;
  }
  * { box-sizing: border-box; margin: 0; padding: 0; }
  html, body { width: 1200px; height: 1024px; overflow: hidden; background: var(--page); }
  body { position: relative; font-family: "PT Sans", Arial, sans-serif; }

  .card { position: absolute; top: 190px; width: 374px; height: 619px; }
  .card--front { left: 200px; background: var(--bark); }
  .card--back { left: 627px; background: var(--amber); }

  .brand-scene {
    position: absolute; left: 55px; top: 22px; width: 264px; height: 118px;
    background: linear-gradient(180deg, #f7b23a 0%, #ee7d1d 55%, #3a1b0c 100%);
  }
  .brand-name {
    position: absolute; left: 0; top: 146px; width: 100%; text-align: center;
    color: var(--white); font-weight: 700; font-size: 30px; letter-spacing: 0.5px;
  }
  .person-name {
    position: absolute; left: 0; top: 198px; width: 100%; text-align: center;
    color: var(--white); font-weight: 700; font-size: 20px;
  }
  .person-title {
    position: absolute; left: 0; top: 228px; width: 100%; text-align: center;
    color: var(--amber-text); font-size: 22px;
  }
  .contact { position: absolute; left: 0; width: 100%; text-align: center; font-size: 19px; white-space: nowrap; }
  .contact--web { font-size: 15.5px; }
  .contact b { color: var(--white); font-weight: 700; }
  .contact span { color: var(--amber-text); }

  .tagline-box {
    position: absolute; left: 55px; top: 0; width: 262px; height: 168px;
    background: var(--bark); color: var(--amber);
    display: flex; flex-direction: column; justify-content: center; align-items: center;
    font-size: 22px; line-height: 1.45; text-align: center; padding-top: 6px;
  }
  .diet {
    position: absolute; left: 0; width: 100%; text-align: center;
    font-size: 29px; color: var(--bark);
  }
  .diet b { font-weight: 700; }

  .side-label {
    position: absolute; top: 850px; width: 374px; text-align: center;
    font-size: 19px; color: var(--label); letter-spacing: 0.5px;
  }
</style>
</head>
<body>
  <section class="card card--front">
    <div class="brand-scene" role="img" aria-label="Sunset savanna scene with dog silhouette and acacia tree"></div>
    <div class="brand-name">Meadowtail Pet</div>
    <div class="person-name">RAVI WELBY</div>
    <div class="person-title">Customer experience officer</div>
    <p class="contact contact--web" style="top:330px"><b>EMAIL:</b><span>rwelby@meadowtailpet-example.net</span></p>
    <p class="contact contact--web" style="top:371px"><b>WEBSITE:</b><span>www.meadowtailpet-example.net</span></p>
    <p class="contact" style="top:452px"><b>TOLL FREE:</b><span>xxx-xxx-xxxx</span></p>
    <p class="contact" style="top:494px"><b>SALES INQUIRIES:</b><span>(800)xxx-xxxx</span></p>
    <p class="contact" style="top:531px"><b>DIRECT:</b><span>(347)xxx-xxxx</span></p>
  </section>

  <section class="card card--back">
    <div class="tagline-box">
      <span>100% NATURAL</span>
      <span>RAW DOG FOOD</span>
    </div>
    <p class="diet" style="top:204px"><b>COMBINATION</b>&nbsp; DIET</p>
    <p class="diet" style="top:303px"><b>CHICKEN</b> DIET</p>
    <p class="diet" style="top:401px"><b>BEEF</b> DIET</p>
    <p class="diet" style="top:499px"><b>LAMB</b> DIET</p>
  </section>

  <p class="side-label" style="left:200px">FRONT</p>
  <p class="side-label" style="left:627px">BACK</p>
</body>
</html>
```